"MEET THE TEAM" page web design

We need a "meet the team" page for our website!
Please look at our website to see the style we need

We are looking for something unique, fun, cool, technology-style and yet professional. We plan on taking a picture of each employee (not sure if this will be a real photo/caricature/ black and white/goofy picture--> but we are open to any ideas you have that will work with the design) and putting it there, along with a little bio about each person.

Thanks! looking forward to working together:)
Updates

Project Deadline Extended
Reason: I am excited to see more designs and find the perfect fit. Thanks designers :)

Target Market(s)

People looking to purchase servers, workstations, components

Industry/Entity Type

Information Technology

Number of Pages Required

1 page

Font styles to use
Sans Serif
Other font styles liked:
• The font we use on our site so it matches

Requirements
Must have
• please look at our website qondimex.com and see the theme and colors we want.
• We have 13 employees but would like to have a design where we can add/remove people if we hire/terminate them without messing up the design.
• We are looking for something unique, fun, cool, technology-style and yet professional. We plan on taking a picture of each employee (not sure if this will be a real photo/caricature/ black and white/goofy picture--> but we are open to any ideas you have that will work with the design) and putting it there, along with a little bio about each person.
• We can upload anything you need
Nice to have
• We are also interested in having a design where when the cursor moves over a person then the bio comes out or moves around, or something. (This is not required, but we would love some cool ideas) And if you can come up with some design, we would have our programmers create it for us.
Should not have
• we are open to anything

```html
<!DOCTYPE html>
<html lang="en">
<head>
<meta charset="utf-8">
<title>Meet Our Team – Qondimex</title>
<link rel="stylesheet" href="https://fonts.googleapis.com/css2?family=Arimo:ital,wght@0,400;0,700;1,400&family=Source+Sans+3:wght@400;600&display=swap">
<style>
  :root {
    --teal: #3ccbbb;
    --ink: #2f3c44;
    --ink-soft: #555;
    --header-bg: #e8e6e6;
    --card-bg: #e9e9e9;
    --card-line: #c9c9c9;
    --card-accent: #c9a3b8;
    --tone-light: #d3d7da;
    --tone-mid: #b4bbc0;
    --tone-dark: #7d8890;
    --tone-deep: #55616a;
    --footer-bg: #2d3a3f;
    --social-1: #3b5998;
    --social-2: #0e76a8;
    --social-3: #55acee;
    --social-muted: #c4c4c4;
  }
  * { box-sizing: border-box; }
  html, body { margin: 0; padding: 0; }
  body {
    width: 1200px; height: 2908px; overflow: hidden; position: relative;
    background: #fff; font-family: "Arimo", Arial, sans-serif; color: var(--ink);
  }
  .site-header {
    position: absolute; left: 0; top: 0; width: 1200px; height: 101px;
    background: var(--header-bg); display: flex; align-items: center; justify-content: center;
    font-size: 52px; font-weight: 700; color: #4a4a4a; letter-spacing: 1px;
  }
  .breadcrumb-bar {
    position: absolute; left: 0; top: 110px; width: 1200px; height: 43px;
    background: var(--teal); font-size: 12px; font-weight: 700; color: var(--ink);
    padding-left: 161px; line-height: 43px;
  }
  .breadcrumb-bar .home { color: #fff; }
  .intro { position: absolute; left: 0; top: 212px; width: 1200px; text-align: center; }
  .intro h1 { margin: 0; font-size: 29px; font-weight: 700; color: var(--ink); letter-spacing: .3px; }
  .intro h1 .brand { color: var(--teal); }
  .intro p { margin: 12px 0 0; font-size: 17px; font-weight: 700; color: var(--ink-soft); }

  .team-grid {
    position: absolute; left: 161px; top: 388px;
    display: grid; grid-template-columns: repeat(3, 268px); grid-auto-rows: 339px;
    column-gap: 37px; row-gap: 36px;
  }
  .card {
    position: relative; background: var(--card-bg);
    border: 1px solid var(--card-line); border-bottom: 2px solid var(--card-accent);
  }
  .card .portrait {
    position: absolute; left: 34px; top: 22px; width: 198px; height: 196px;
    border-radius: 90px 90px 22px 22px;
  }
  .portrait--light { background: linear-gradient(180deg, var(--tone-light) 0%, #c6cbcf 100%); }
  .portrait--mid { background: linear-gradient(180deg, var(--tone-mid) 0%, #a3abb1 100%); }
  .portrait--dark { background: linear-gradient(180deg, var(--tone-dark) 0%, #6b767e 100%); }
  .portrait--deep { background: linear-gradient(180deg, var(--tone-deep) 0%, #46525b 100%); }
  .card .base {
    position: absolute; left: 0; right: 0; bottom: 0; height: 96px; background: #fff;
    clip-path: polygon(0 44%, 100% 0, 100% 100%, 0 100%);
  }
  .social {
    position: absolute; left: 0; right: 0; bottom: 18px;
    display: flex; justify-content: center; gap: 16px;
  }
  .social span { width: 21px; height: 21px; border-radius: 50%; display: block; }
  .social .s1 { background: var(--social-1); }
  .social .s2 { background: var(--social-2); }
  .social .s3 { background: var(--social-3); }
  .social .muted { background: var(--social-muted); }

  .card--featured { background: var(--teal); border-color: var(--teal); border-bottom-color: var(--card-accent); }
  .name-tag {
    position: absolute; left: 47px; top: -30px; width: 168px; height: 278px;
    background: #fff; border: 1px solid #d6d6d6; text-align: center; z-index: 2;
  }
  .name-tag .avatar {
    width: 120px; height: 120px; border-radius: 50%; background: #8a8a8a; margin: 38px auto 0;
  }
  .name-tag .rule { width: 22px; height: 1px; background: #bbb; margin: 8px auto 0; }
  .name-tag .name { font-size: 17px; font-weight: 700; margin-top: 14px; }
  .name-tag .role { font-size: 13px; margin-top: 4px; }
  .fold { position: absolute; top: -30px; width: 0; height: 0; z-index: 1; }
  .fold--left { left: 31px; border-right: 16px solid #bdbdbd; border-top: 30px solid transparent; }
  .fold--right { left: 215px; border-left: 16px solid #bdbdbd; border-top: 30px solid transparent; }

  .card--promo {
    display: flex; flex-direction: column; align-items: center; justify-content: center;
    border-bottom: 1px solid var(--card-line); text-align: center;
    font-family: "Source Sans 3", "Arimo", sans-serif; color: #555;
  }
  .card--story .label { font-size: 29px; margin-top: 20px; }
  .card--review .label { font-size: 36px; line-height: 1.05; margin-top: 28px; }
  .card--review .label em { font-style: normal; color: var(--teal); }

  .join { position: absolute; left: 161px; top: 2296px; width: 600px; }
  .join h2 { margin: 0; font-size: 30px; font-weight: 700; color: var(--ink); }
  .join p { margin: 44px 0 0; font-size: 12px; line-height: 24px; color: #444; }
  .join .note { margin-top: 36px; font-size: 12px; font-style: italic; color: #222; }
  .join .note a { color: var(--teal); }
  .vacancy-card {
    position: absolute; left: 861px; top: 2314px; width: 144px; height: 183px;
    background: var(--card-bg); border: 1px solid var(--card-line); border-bottom: 2px solid var(--card-accent);
  }
  .vacancy-card .text { position: absolute; top: 44px; width: 100%; text-align: center; font-size: 12px; font-weight: 700; }
  .vacancy-card .base { position: absolute; left: 0; right: 0; bottom: 0; height: 52px; background: #fff; clip-path: polygon(0 44%, 100% 0, 100% 100%, 0 100%); }
  .vacancy-card .social { bottom: 8px; gap: 6px; }
  .vacancy-card .social span { width: 12px; height: 12px; }

  .site-footer {
    position: absolute; left: 0; top: 2588px; width: 1200px; height: 320px;
    background: var(--footer-bg); display: flex; align-items: center; justify-content: center;
    font-size: 52px; font-weight: 700; color: #fff; letter-spacing: 1px;
  }
</style>
</head>
<body>
  <header class="site-header">HEADER</header>
  <nav class="breadcrumb-bar"><span class="home">Home</span>/Meet Our Team</nav>

  <section class="intro">
    <h1>THE FACES OF THE <span class="brand">QONDIMEX</span></h1>
    <p>Meet our most talented and ambitious magic makers people</p>
  </section>

  <main class="team-grid">
    <article class="card card--featured">
      <span class="fold fold--left"></span><span class="fold fold--right"></span>
      <div class="name-tag">
        <div class="avatar"></div>
        <div class="rule"></div>
        <div class="name">John Doe</div>
        <div class="role">Project manager</div>
      </div>
      <div class="base"></div>
      <div class="social"><span class="muted"></span><span class="s2"></span><span class="s3"></span></div>
    </article>

    <article class="card"><div class="portrait portrait--light" role="img" aria-label="Line-art avatar of a team member with hair in a bun"></div><div class="base"></div><div class="social"><span class="s1"></span><span class="s2"></span><span class="s3"></span></div></article>
    <article class="card"><div class="portrait portrait--light" role="img" aria-label="Line-art avatar of a team member in a hat, glasses and jacket"></div><div class="base"></div><div class="social"><span class="s1"></span><span class="s2"></span><span class="s3"></span></div></article>
    <article class="card"><div class="portrait portrait--dark" role="img" aria-label="Filled avatar of a team member with a bob haircut"></div><div class="base"></div><div class="social"><span class="s1"></span><span class="s2"></span><span class="s3"></span></div></article>
    <article class="card"><div class="portrait portrait--light" role="img" aria-label="Line-art avatar of a team member with spiky hair and glasses"></div><div class="base"></div><div class="social"><span class="s1"></span><span class="s2"></span><span class="s3"></span></div></article>

    <article class="card card--promo card--story">
      <svg width="118" height="118" viewBox="0 0 120 120" aria-hidden="true">
        <circle cx="60" cy="60" r="60" fill="#3ccbbb"/>
        <polygon points="45,32 45,88 92,60" fill="#fff"/>
      </svg>
      <div class="label">Our success story</div>
    </article>

    <article class="card"><div class="portrait portrait--mid" role="img" aria-label="Avatar of a team member with glasses and a polo shirt"></div><div class="base"></div><div class="social"><span class="s1"></span><span class="s2"></span><span class="s3"></span></div></article>
    <article class="card"><div class="portrait portrait--deep" role="img" aria-label="Avatar of a bearded team member in sunglasses"></div><div class="base"></div><div class="social"><span class="s1"></span><span class="s2"></span><span class="s3"></span></div></article>
    <article class="card"><div class="portrait portrait--mid" role="img" aria-label="Avatar of a team member in shirt and tie"></div><div class="base"></div><div class="social"><span class="s1"></span><span class="s2"></span><span class="s3"></span></div></article>
    <article class="card"><div class="portrait portrait--deep" role="img" aria-label="Avatar of a team member with a goatee in a suit"></div><div class="base"></div><div class="social"><span class="s1"></span><span class="s2"></span><span class="s3"></span></div></article>
    <article class="card"><div class="portrait portrait--mid" role="img" aria-label="Avatar of a bearded team member with glasses"></div><div class="base"></div><div class="social"><span class="s1"></span><span class="s2"></span><span class="s3"></span></div></article>
    <article class="card"><div class="portrait portrait--dark" role="img" aria-label="Avatar of a team member in a crew-neck top"></div><div class="base"></div><div class="social"><span class="s1"></span><span class="s2"></span><span class="s3"></span></div></article>
    <article class="card"><div class="portrait portrait--mid" role="img" aria-label="Avatar of a team member in a cap and polo shirt"></div><div class="base"></div><div class="social"><span class="s1"></span><span class="s2"></span><span class="s3"></span></div></article>

    <article class="card card--promo card--review">
      <svg width="118" height="92" viewBox="0 0 118 92" aria-hidden="true">
        <path d="M8 8 Q30 0 56 10 V80 Q30 70 8 78 Z" fill="#3ccbbb"/>
        <path d="M110 8 Q88 0 62 10 V80 Q88 70 110 78 Z" fill="#3ccbbb"/>
        <path d="M2 16 V88 H116 V16" fill="none" stroke="#3ccbbb" stroke-width="4"/>
      </svg>
      <div class="label">Read <em>2016</em><br>Year review</div>
    </article>

    <article class="card"><div class="portrait portrait--deep" role="img" aria-label="Avatar of a team member with curly hair"></div><div class="base"></div><div class="social"><span class="s1"></span><span class="s2"></span><span class="s3"></span></div></article>
  </main>

  <section class="join">
    <h2>JOIN OUR TEAM</h2>
    <p>Lorem ipsum dolor sit amet, consectetur adipisicing elit, sed do eiusmod tempor incididunt ut labore et dolore magna aliqua. Ut enim ad minim veniam, quis nostrud exercitation ullamco laboris nisi ut aliquip ex ea commodo consequat. Duis aute irure dolor in repreheure dolor in repreheure dolor in repreheure dolor in reprehenderit in voluptate v</p>
    <div class="note">There are currently no open positions. But you're welcome to <a href="#">email us</a> and introduce yourself!</div>
  </section>

  <aside class="vacancy-card">
    <div class="text">It could be you!</div>
    <div class="base"></div>
    <div class="social"><span class="s1"></span><span class="s2"></span><span class="s3"></span></div>
  </aside>

  <footer class="site-footer">FOOTER</footer>
</body>
</html>
```